MINIMAL Design Alteration for a UI/UX design

- Below is the Sketch file as well the logo for a UI/UX infrustructure for an application that enables users to book instant cleaning services. However when it was started the project enabled users to book a wide variety of services. The logo includes a mop as well as a hammer. We want the designer to do the following two small edits on the platform. Them being :
1. Edit the logo as to include the mop and another symbol of cleaning in a visually appealing manner
2. Modify the UI/UX screen in the sketch file removing the other services and only maintaining the cleaning option in A VISUALLY APPEALING MANNER
Any useful edits would be appreciated !

best

Requirements
Must have
• ABILITY TO BOOK CLEANING SERVICE ONLY IN A APPEALING MANNER

```html
<!DOCTYPE html>
<html lang="en">
<head>
<meta charset="utf-8">
<title>tidynest – welcome screen</title>
<link rel="stylesheet" href="https://fonts.googleapis.com/css2?family=Dosis:wght@400;600;700&display=swap">
<style>
  :root {
    --page-bg: #ecebe8;
    --screen-green-top: #bde564;
    --screen-green-bottom: #a9d35a;
    --accent-green: #9ccb4d;
    --white: #ffffff;
    --white-soft: rgba(255, 255, 255, 0.78);
    --tab-bg: #ffffff;
    --tab-ink: #8e8e8e;
    --illustration-tone: rgba(255, 255, 255, 0.28);
  }
  * { box-sizing: border-box; margin: 0; padding: 0; }
  html, body {
    width: 1200px;
    height: 1000px;
    overflow: hidden;
    background: var(--page-bg);
    font-family: "Dosis", sans-serif;
  }
  .app-screen {
    position: absolute;
    left: 350px;
    top: 50px;
    width: 500px;
    height: 900px;
    background: linear-gradient(180deg, var(--screen-green-top), var(--screen-green-bottom));
    overflow: hidden;
    box-shadow: 0 10px 40px rgba(0, 0, 0, 0.12);
  }
  .welcome-illustration {
    position: absolute;
    left: 140px;
    top: 90px;
    width: 220px;
    height: 210px;
    border-radius: 18px;
    background: radial-gradient(circle at 50% 45%, var(--illustration-tone), rgba(255,255,255,0.06) 70%);
  }
  .welcome-title {
    position: absolute;
    top: 335px;
    width: 100%;
    text-align: center;
    color: var(--white);
    line-height: 1.05;
  }
  .welcome-title .lead {
    display: block;
    font-weight: 400;
    font-size: 42px;
    letter-spacing: 0.5px;
  }
  .welcome-title .brand-name {
    display: block;
    font-weight: 700;
    font-size: 44px;
  }
  .first-step-hint {
    position: absolute;
    top: 478px;
    width: 100%;
    text-align: center;
    color: var(--white-soft);
    font-size: 30px;
    line-height: 1.15;
  }
  .first-step-hint strong { font-weight: 700; }
  .hint-arrow {
    position: absolute;
    left: 210px;
    top: 575px;
  }
  .tab-bar {
    position: absolute;
    left: 0;
    bottom: 0;
    width: 100%;
    height: 95px;
    background: var(--tab-bg);
    display: flex;
    align-items: flex-end;
    justify-content: space-between;
    padding: 0 8px 14px;
  }
  .tab-item {
    width: 80px;
    display: flex;
    flex-direction: column;
    align-items: center;
    gap: 6px;
    color: var(--tab-ink);
    font-size: 13px;
    font-weight: 600;
  }
  .tab-item.is-active { color: var(--accent-green); }
  .tab-spacer { width: 130px; }
  .add-reservation-button {
    position: absolute;
    left: 50%;
    top: -22px;
    width: 120px;
    height: 120px;
    margin-left: -60px;
    border-radius: 50%;
    background: var(--accent-green);
    border: 4px solid var(--white);
    display: flex;
    align-items: center;
    justify-content: center;
  }
</style>
</head>
<body>
  <main class="app-screen">
    <div class="welcome-illustration" role="img" aria-label="Line illustration of cleaning supplies: a bucket with soap bubbles, a mop, a squeegee and a broom in front of a house outline"></div>

    <h1 class="welcome-title">
      <span class="lead">welcome to</span>
      <span class="brand-name">tidynest!</span>
    </h1>

    <p class="first-step-hint">tap <strong>+</strong> to make your<br><strong>first reservation!</strong></p>

    <svg class="hint-arrow" width="80" height="70" viewBox="0 0 80 70" fill="none" stroke="rgba(255,255,255,0.78)" stroke-width="3" stroke-linecap="round" stroke-linejoin="round">
      <path d="M68 4 C72 28 52 36 40 40 C26 44 18 50 22 62"/>
      <path d="M12 52 L22 63 L30 52"/>
    </svg>

    <nav class="tab-bar">
      <div class="tab-item is-active">
        <svg width="34" height="30" viewBox="0 0 34 30" fill="none" stroke="currentColor" stroke-width="2">
          <rect x="2" y="4" width="30" height="24" rx="2"/>
          <line x1="2" y1="11" x2="32" y2="11"/>
          <line x1="9" y1="1" x2="9" y2="7"/>
          <line x1="25" y1="1" x2="25" y2="7"/>
          <rect x="20" y="17" width="7" height="6"/>
        </svg>
        <span>reservations</span>
      </div>
      <div class="tab-item">
        <svg width="30" height="30" viewBox="0 0 30 30" fill="none" stroke="currentColor" stroke-width="2">
          <path d="M18 4 H4 V26 H26 V12"/>
          <circle cx="25" cy="5" r="3.5"/>
        </svg>
        <span>notifications</span>
      </div>
      <div class="tab-spacer"></div>
      <div class="tab-item">
        <svg width="28" height="30" viewBox="0 0 28 30" fill="none" stroke="currentColor" stroke-width="2">
          <circle cx="14" cy="9" r="6"/>
          <path d="M3 28 V25 C3 19 8 17 14 17 C20 17 25 19 25 25 V28 Z"/>
        </svg>
        <span>account</span>
      </div>
      <div class="tab-item">
        <svg width="30" height="30" viewBox="0 0 30 30" fill="currentColor">
          <circle cx="6" cy="18" r="2.5"/>
          <circle cx="15" cy="18" r="2.5"/>
          <circle cx="24" cy="18" r="2.5"/>
        </svg>
        <span>more</span>
      </div>

      <div class="add-reservation-button" aria-label="new reservation">
        <svg width="46" height="46" viewBox="0 0 46 46" stroke="#ffffff" stroke-width="7" stroke-linecap="round">
          <line x1="23" y1="5" x2="23" y2="41"/>
          <line x1="5" y1="23" x2="41" y2="23"/>
        </svg>
      </div>
    </nav>
  </main>
</body>
</html>
```